Homebrew-webshop picture design

I need help with catogory-pics and frontpage-pics for my homebrew-webshop: http://maltkisten.test47.webfjordhost.dk/

My main buiness is raw materials and equipment for small scale beer-brewing.
I would like the pics is welcoming and descriptive.
Cues: Quality products, Customer Care, Personal service,

```html
<!DOCTYPE html>
<html lang="en">
<head>
<meta charset="utf-8">
<title>Maltkisten dk – Homebrew Webshop</title>
<link rel="stylesheet" href="https://fonts.googleapis.com/css2?family=Poppins:wght@400;500;600&display=swap">
<style>
:root{
  --blue:#1257b0;
  --blue-dark:#0d4a99;
  --ink:#333333;
  --muted:#555555;
  --topbar:#e9eaec;
  --line:#dddddd;
  --star:#f08a1c;
  --footer:#141414;
  --white:#ffffff;
}
*{box-sizing:border-box;margin:0;padding:0}
html,body{width:1200px;height:3922px;overflow:hidden}
body{position:relative;background:var(--white);font-family:Arial,Helvetica,sans-serif;color:var(--ink)}
.abs{position:absolute}
.heading-font{font-family:'Poppins',sans-serif}

/* top bar */
.topbar{left:0;top:0;width:1200px;height:46px;background:var(--topbar);font-family:'Poppins',sans-serif;font-size:11px;font-weight:600;color:#333}
.topbar .call{left:111px;top:15px}
.topbar .links{right:111px;top:15px;display:flex;gap:20px}
.topbar .links span{display:flex;align-items:center;gap:6px}

/* header */
.header{left:0;top:46px;width:1200px;height:111px}
.logo{left:111px;top:28px;font-family:'Poppins',sans-serif;font-size:34px;font-weight:500;color:var(--blue);letter-spacing:-0.5px}
.search{left:535px;top:37px;width:554px;height:43px;border:1px solid #cfcfcf;display:flex}
.search .field{flex:1;font-size:11px;color:#666;padding:13px 14px}
.search .btn{width:53px;background:var(--blue);display:flex;align-items:center;justify-content:center}

/* nav */
.nav{left:0;top:157px;width:1200px;height:58px;background:var(--blue);border-bottom:3px solid #0a3f85}
.nav ul{list-style:none;display:flex;position:absolute;left:111px;top:0;height:55px;font-family:'Poppins',sans-serif;font-size:14px;color:#fff}
.nav li{padding:0 19px;line-height:55px}
.nav li.active{background:#333;padding:0 33px}

/* hero */
.hero{left:0;top:215px;width:1200px;height:653px;background:radial-gradient(circle at 50% 35%,#6b4a2a 0%,#3b2a1a 45%,#1e150d 100%)}
.hero h1{left:0;top:255px;width:1200px;text-align:center;font-family:'Poppins',sans-serif;font-weight:600;font-size:68px;color:#fff}
.hero p{left:300px;top:350px;width:600px;text-align:center;font-family:'Poppins',sans-serif;font-weight:500;font-size:22px;line-height:39px;color:#fff}
.hero .cta{left:528px;top:446px;width:142px;height:47px;background:var(--blue);color:#fff;font-family:'Poppins',sans-serif;font-weight:600;font-size:16px;display:flex;align-items:center;justify-content:center}

/* section titles */
.section-title{left:0;width:1200px;text-align:center;font-family:'Poppins',sans-serif;font-weight:500;font-size:33px;color:var(--ink)}
.section-title em{font-style:normal;color:var(--blue)}
.section-sub{left:0;width:1200px;text-align:center;font-size:15px;color:var(--muted)}

.welcome-text{left:210px;top:982px;width:780px;text-align:center;font-size:15px;line-height:33px;color:var(--muted)}

/* categories */
.cat{background:linear-gradient(160deg,#8a8f94,#3b3f44)}
.cat-label{position:absolute;left:29px;right:29px;bottom:24px;height:52px;background:rgba(255,255,255,.72);border-top:2px dashed #777;border-bottom:2px dashed #777;display:flex;align-items:center;justify-content:center;font-family:'Poppins',sans-serif;font-weight:500;font-size:17px;color:#333;letter-spacing:.5px}

/* products */
.product{width:229px;height:370px;border:1px solid var(--line);text-align:center;font-family:'Poppins',sans-serif}
.product .shot{position:absolute;left:6px;top:6px;right:6px;height:192px;background:radial-gradient(circle,#e6e6e6,#f7f7f7);border:1px solid #eee}
.product .name{position:absolute;left:0;right:0;top:222px;font-size:16px;font-weight:500;color:#333}
.product .stars{position:absolute;left:0;right:0;top:248px;font-size:15px;color:var(--star);letter-spacing:2px}
.product .price{position:absolute;left:0;right:0;top:275px;font-size:17px;font-weight:500;color:var(--blue)}
.product .add{position:absolute;left:45px;top:308px;width:137px;height:40px;border:1px solid #555;display:flex;align-items:center;justify-content:center;font-size:13px;color:#333}

/* features band */
.band{left:0;top:2722px;width:1200px;height:304px;background:var(--blue)}
.feature{width:330px;text-align:center;color:#fff}
.feature svg{display:block;margin:0 auto}
.feature h3{margin-top:22px;font-family:'Poppins',sans-serif;font-weight:500;font-size:23px}
.feature p{margin-top:10px;font-size:13px;line-height:25px}

/* blog */
.post{width:309px;height:360px;text-align:center}
.post .pic{position:absolute;left:0;top:0;width:100%;height:252px;background:linear-gradient(160deg,#c98a3a,#5a3414)}
.post .date{position:absolute;left:16px;right:16px;top:229px;height:40px;background:#fff;padding-top:16px;font-family:'Poppins',sans-serif;font-size:18px;color:var(--blue)}
.post .title{position:absolute;left:20px;right:20px;top:276px;font-family:'Poppins',sans-serif;font-size:18px;line-height:26px;color:#333}

/* footer */
.footer{left:0;top:3584px;width:1200px;height:338px;background:var(--footer);color:#fff}
.footer h4{position:absolute;top:54px;font-family:Arial,sans-serif;font-weight:700;font-size:15px;letter-spacing:.3px}
.footer ul{position:absolute;top:92px;list-style:none;font-size:11px;line-height:26px}
.footer li::before{content:"";display:inline-block;border-left:5px solid #fff;border-top:4px solid transparent;border-bottom:4px solid transparent;margin-right:20px;vertical-align:middle}
.cards{left:111px;top:90px;display:flex;gap:5px}
.cards span{width:40px;height:24px;background:#dfe3ea;border-radius:2px}
.social{left:111px;top:178px;display:flex;gap:7px}
.social span{width:36px;height:36px;border:2px solid #fff;border-radius:50%}
.contact{left:918px;top:96px;font-size:11px;line-height:28px}
.contact div{display:flex;gap:14px;align-items:flex-start}
.copyright{left:0;top:3882px;width:1200px;text-align:center;font-size:11px;color:#ddd}
</style>
</head>
<body>

<div class="abs topbar">
  <span class="abs call">CALL US : 000-555-0100</span>
  <div class="abs links">
    <span><svg width="11" height="11" viewBox="0 0 24 24" fill="none" stroke="#333" stroke-width="3"><path d="M12 21l-8-8a5 5 0 0 1 8-6 5 5 0 0 1 8 6z"/></svg>WISHLIST</span>
    <span><svg width="11" height="11" viewBox="0 0 24 24" fill="none" stroke="#333" stroke-width="3"><circle cx="10" cy="10" r="7"/><path d="M15 15l6 6"/></svg>SEARCH</span>
    <span><svg width="11" height="11" viewBox="0 0 24 24" fill="#333"><path d="M2 10h12V5l8 7-8 7v-5H2z"/></svg>SIGN IN</span>
    <span><svg width="12" height="11" viewBox="0 0 24 22" fill="#333"><path d="M0 1h5l3 12h13l3-9H7"/><circle cx="10" cy="19" r="2"/><circle cx="19" cy="19" r="2"/></svg>CART &nbsp;$0.00</span>
  </div>
</div>

<div class="abs header">
  <div class="abs logo">Maltkisten.dk</div>
  <div class="abs search">
    <div class="field">Enter Keyword...</div>
    <div class="btn"><svg width="15" height="15" viewBox="0 0 24 24" fill="none" stroke="#fff" stroke-width="3"><circle cx="10" cy="10" r="7"/><path d="M15 15l6 6"/></svg></div>
  </div>
</div>

<nav class="abs nav">
  <ul>
    <li class="active">Home</li><li>Commodites</li><li>Brewing &amp; Fermentation</li><li>Bottling</li><li>Cleaning</li><li>Laboratoriet</li><li>Books</li><li>Contact us</li>
  </ul>
</nav>

<section class="abs hero" role="img" aria-label="Brewing still life: wooden barrel, hops, lantern, grain sacks and beer bottles">
  <h1 class="abs">Maltkisten dk</h1>
  <p class="abs">Sed ut perspiciatis unde omnis iste natus error sit voluptatem accusantium dolorem</p>
  <div class="abs cta">READ MORE</div>
</section>

<h2 class="abs section-title" style="top:912px">Welcome to <em>Maltkisten dk</em></h2>
<p class="abs welcome-text">Sed ut perspiciatis unde omnis iste natus error sit voluptatem accusantium doloremque laudantium, totam rem aperiam, eaque ipsa quae ab illo inventore veritatis et quasi architecto beatae vitae dicta sunt explicabo. Nemo consequuntur magni dolores eos qui ratione voluptatem sequi nesciunt.</p>

<div class="abs cat" style="left:111px;top:1115px;width:312px;height:266px;background:linear-gradient(160deg,#5a3a1e,#c98a2f 55%,#1b140d)" role="img" aria-label="Glass of beer beside a barrel and wheat"><div class="cat-label">COMMODITIES</div></div>
<div class="abs cat" style="left:443px;top:1115px;width:314px;height:560px;background:linear-gradient(180deg,#4a4c50,#b7b9bb 50%,#6b6d70)" role="img" aria-label="Row of steel fermentation tanks in a brewery"><div class="cat-label">BREWING &amp; FERMENTATION</div></div>
<div class="abs cat" style="left:775px;top:1115px;width:314px;height:266px;background:linear-gradient(160deg,#2a2418,#a07a2c 50%,#1a160f)" role="img" aria-label="Close-up of brown beer bottles"><div class="cat-label">BOTTLING</div></div>
<div class="abs cat" style="left:111px;top:1406px;width:312px;height:269px;background:linear-gradient(180deg,#cfd8e0,#eef2f5)" role="img" aria-label="Clean glass bottles upside down on a rack"><div class="cat-label">CLEANING</div></div>
<div class="abs cat" style="left:775px;top:1406px;width:314px;height:269px;background:linear-gradient(160deg,#9b9c9d,#d7d7d6 55%,#7a6a5c)" role="img" aria-label="Brewing kettle with gauge and copper coil"><div class="cat-label">LABORATORIET</div></div>

<h2 class="abs section-title" style="top:1740px">Featured <em>Products</em></h2>
<p class="abs section-sub" style="top:1797px">Sed ut perspiciatis unde omnis iste natus error sit voluptatem accusantium doloremque</p>

<div class="abs product" style="left:111px;top:1866px"><div class="shot" role="img" aria-label="Pile of malted barley"></div><div class="name">MALT</div><div class="stars">☆☆☆☆☆</div><div class="price">16.00 kr</div><div class="add">ADD TO CART</div></div>
<div class="abs product" style="left:359px;top:1866px"><div class="shot" role="img" aria-label="Bag of grain with recipe kit"></div><div class="name">Mix recipe yourself</div><div class="stars">☆☆☆☆☆</div><div class="price">149.95 kr</div><div class="add">ADD TO CART</div></div>
<div class="abs product" style="left:609px;top:1866px"><div class="shot" role="img" aria-label="Kegerator with gas bottle and keg"></div><div class="name">Kegerator</div><div class="stars">☆☆☆☆☆</div><div class="price">4,549.00</div><div class="add">ADD TO CART</div></div>
<div class="abs product" style="left:857px;top:1866px"><div class="shot" role="img" aria-label="Red bottle drying tree with green bottles"></div><div class="name">MALT</div><div class="stars">☆☆☆☆☆</div><div class="price">16.00 kr</div><div class="add">ADD TO CART</div></div>

<div class="abs product" style="left:111px;top:2286px"><div class="shot" role="img" aria-label="Rotary bottle washer"></div><div class="name">Rotary Bottle Washers</div><div class="stars">☆☆☆☆☆</div><div class="price">16.00 kr</div><div class="add">ADD TO CART</div></div>
<div class="abs product" style="left:359px;top:2286px"><div class="shot" role="img" aria-label="Magnetic stirrer plate"></div><div class="name">Magnetic</div><div class="stars">☆☆☆☆☆</div><div class="price">499,00 kr</div><div class="add">ADD TO CART</div></div>
<div class="abs product" style="left:609px;top:2286px"><div class="shot" role="img" aria-label="Bottle and two glasses of amber beer"></div><div class="name">Edition One Christmas</div><div class="stars">☆☆☆☆☆</div><div class="price">49.95 kr</div><div class="add">ADD TO CART</div></div>
<div class="abs product" style="left:857px;top:2286px"><div class="shot" role="img" aria-label="Brewing kettle with black insulation sheath"></div><div class="name">Insulation Sheath</div><div class="stars">☆☆☆☆☆</div><div class="price">349.00 kr</div><div class="add">ADD TO CART</div></div>

<section class="abs band">
  <div class="abs feature" style="left:105px;top:62px">
    <svg width="70" height="84" viewBox="0 0 70 84" fill="none" stroke="#fff" stroke-width="2.5"><circle cx="35" cy="33" r="28"/><circle cx="35" cy="33" r="20"/><path d="M20 58l-8 22 10-5 6 8 6-20M50 58l8 22-10-5-6 8-6-20"/><path d="M27 32h6v12h-6zM33 32l5-9h3v8h6l-2 13H33"/></svg>
    <h3>Quality Products</h3>
    <p>Sed ut perspiciatis unde omnis iste natus<br>error sit voluptatem accusantium</p>
  </div>
  <div class="abs feature" style="left:435px;top:62px">
    <svg width="84" height="84" viewBox="0 0 84 84" fill="none" stroke="#fff" stroke-width="2.5"><rect x="10" y="4" width="36" height="26" rx="3"/><path d="M17 12h22M17 18h22M17 24h14"/><path d="M22 36c0 22 14 36 34 40l4-10-10-6-6 6c-8-4-12-10-14-18l6-6-6-10z"/><path d="M62 38a10 10 0 0 1 0 20"/></svg>
    <h3>Customer Care</h3>
    <p>Sed ut perspiciatis unde omnis iste natus<br>error sit voluptatem accusantium</p>
  </div>
  <div class="abs feature" style="left:766px;top:62px">
    <svg width="84" height="84" viewBox="0 0 84 84" fill="none" stroke="#fff" stroke-width="2.5"><path d="M8 14a14 14 0 0 0 18 18l40 40 6-6-40-40A14 14 0 0 0 14 8l8 8-2 6-6 2z"/><path d="M60 8l12 4 4 12-24 24-16-16z"/><path d="M36 44L14 66l6 6 22-22"/></svg>
    <h3>Personal Service</h3>
    <p>Sed ut perspiciatis unde omnis iste natus<br>error sit voluptatem accusantium</p>
  </div>
</section>

<h2 class="abs section-title" style="top:3075px">Latest <em>Blog</em></h2>
<p class="abs section-sub" style="top:3133px">Sed ut perspiciatis unde omnis iste natus error sit voluptatem accusantium doloremque</p>

<div class="abs post" style="left:111px;top:3198px"><div class="pic" role="img" aria-label="Glasses of beer in front of bar taps"></div><div class="date">29 June 2020</div><div class="title">Sed ut perspiciatis unde is<br>te natus error sit</div></div>
<div class="abs post" style="left:445px;top:3198px"><div class="pic" role="img" aria-label="Three dark and amber beers on a table" style="background:linear-gradient(160deg,#2a1a10,#b0661e 55%,#1a0f08)"></div><div class="date">29 June 2020</div><div class="title">Sed ut perspiciatis unde is<br>te natus error sit</div></div>
<div class="abs post" style="left:778px;top:3198px"><div class="pic" role="img" aria-label="Glasses of pale beer with snacks" style="background:linear-gradient(160deg,#7a4a1e,#e0a33c 55%,#4a2a10)"></div><div class="date">29 June 2020</div><div class="title">Sed ut perspiciatis unde is<br>te natus error sit</div></div>

<footer class="abs footer">
  <h4 style="left:111px">PAYMENTS ACCEPTED</h4>
  <div class="abs cards"><span></span><span></span><span></span><span></span></div>
  <div class="abs social"><span></span><span></span><span></span><span></span><span></span></div>

  <h4 style="left:361px">CUSTOMER SERVICE</h4>
  <ul style="left:361px"><li>Frequently asked questions</li><li>trading Terms</li><li>Privacy Policy</li><li>Here you find us</li><li>Contact us</li></ul>

  <h4 style="left:567px">INFORMATION</h4>
  <ul style="left:567px"><li>Information</li><li>Om os</li><li>Sådan handler du</li><li>Sikker handel</li><li>Vejledning</li></ul>

  <h4 style="left:754px">MY ACCOUNT</h4>
  <ul style="left:754px"><li>My account</li><li>Orders</li><li>Addresses</li><li>Shopping cart</li><li>Wishlist</li></ul>

  <h4 style="left:918px">CONTACT US</h4>
  <div class="abs contact">
    <div><svg width="13" height="13" viewBox="0 0 24 24" fill="#fff"><path d="M6 2l4 5-2 3c2 3 3 4 6 6l3-2 5 4-3 4C10 21 3 14 2 5z"/></svg>40 11 22 33 (Phone)</div>
    <div><svg width="13" height="13" viewBox="0 0 24 24" fill="#fff"><rect x="6" y="2" width="12" height="6"/><rect x="2" y="9" width="20" height="9"/><rect x="6" y="15" width="12" height="7" fill="#141414" stroke="#fff" stroke-width="2"/></svg>40 11 22 33 &nbsp;&nbsp;(Fax)</div>
    <div><svg width="13" height="13" viewBox="0 0 24 24" fill="#fff"><path d="M2 5h20v14H2z"/><path d="M2 5l10 8 10-8" stroke="#141414" stroke-width="2" fill="none"/></svg><span style="text-decoration:underline">info@maltkisten.dk</span></div>
    <div style="line-height:16px;margin-top:6px"><svg width="13" height="16" viewBox="0 0 24 30" fill="#fff"><path d="M12 0a10 10 0 0 1 10 10c0 8-10 20-10 20S2 18 2 10A10 10 0 0 1 12 0z"/><circle cx="12" cy="10" r="4" fill="#141414"/></svg>Maltkisten Kornvejen 14<br>8800 Bøgely</div>
  </div>
</footer>
<div class="abs copyright">© Copyright 2020 Nordlys Webshop All Rights Reserved</div>

</body>
</html>
```